Covid19 Poster for workplaces

Create a poster on how to protect yourself from Corona virus at work.
We are a Kindred Works company. We have just re-branded so we need to fit in with our brand. We like clean and fresh, slightly amusing is ok if it will draw attention but it's an important topic. A4 and A3 please.

Content:

Headline: Lower the risk of COVID 19 in the workplace.

BE WELL

Bring your own cup - don’t share cups and food.
Elbow tap instead of handshakes and kisses
Wash your hands often - with soap.
Elbow or tissues when you cough or sneeze then straight in the bin
Leave your face alone after touching shared surfaces
Leave your bugs at home if you’re feeling unwell.

Call health line if you have a cough, a high temperature and shortness of breath. 0800 472 9160

Based on recommendations from IPB and DCT

Target Market(s)

Employees - so anyone

Other font styles liked:
• Use the closest font to the brand documents

Requirements
Should not have
• Clip art

```html
<!DOCTYPE html>
<html lang="en">
<head>
<meta charset="utf-8">
<title>Lower the risk of COVID 19 in the workplace</title>
<link rel="stylesheet" href="https://fonts.googleapis.com/css2?family=Arimo:wght@400;700&display=swap">
<style>
  :root {
    --green: #8dc63f;
    --white: #ffffff;
    --ink: #111111;
    --teal: #19a9b8;
    --icon-fill: rgba(255, 255, 255, 0.28);
  }
  * { margin: 0; padding: 0; box-sizing: border-box; }
  html, body { width: 849px; height: 1200px; overflow: hidden; }
  body { background: var(--green); font-family: "Arimo", Arial, sans-serif; color: var(--white); }
  .poster { position: relative; width: 849px; height: 1200px; background: var(--green); }

  .headline {
    position: absolute; left: 67px; top: 46px;
    font-size: 43px; line-height: 45px; font-weight: 400; letter-spacing: -0.8px;
  }
  .rule { position: absolute; height: 1px; background: var(--white); }
  .rule-top { left: 72px; top: 160px; width: 485px; }
  .rule-mid { left: 72px; top: 299px; width: 485px; }
  .rule-foot { left: 72px; top: 1036px; width: 709px; }

  .title {
    position: absolute; left: 68px; top: 162px;
    font-size: 123px; line-height: 130px; font-weight: 700; letter-spacing: -6px;
  }

  .timeline-spine { position: absolute; left: 72px; top: 299px; width: 1px; height: 561px; background: var(--white); }
  .tick { position: absolute; left: 72px; width: 20px; height: 1px; background: var(--white); }

  .tip-icon {
    position: absolute; left: 116px; width: 62px; height: 62px;
    border-radius: 10px; background: var(--icon-fill);
  }
  .tip-text {
    position: absolute; left: 202px;
    font-size: 25px; line-height: 29px; font-weight: 400; letter-spacing: -0.2px;
  }

  .healthline {
    position: absolute; left: 73px; top: 942px;
    font-size: 26.5px; line-height: 38px; font-weight: 700; letter-spacing: -0.3px;
  }
  .credits-label {
    position: absolute; left: 73px; top: 1056px;
    font-size: 17px; line-height: 20px; font-weight: 700;
  }

  .partner { position: absolute; top: 1096px; height: 54px; display: flex; align-items: center; gap: 12px; }
  .partner-dct { left: 73px; }
  .partner-ipb { left: 235px; }
  .partner-shape { width: 40px; height: 40px; border: 1.5px solid var(--white); }
  .partner-ipb .partner-shape { border-radius: 50%; }
  .partner-name { font-size: 28px; font-weight: 400; letter-spacing: 1px; }

  .client { position: absolute; left: 538px; top: 1096px; height: 56px; display: flex; align-items: center; gap: 14px; }
  .client-mark { width: 52px; height: 52px; border-radius: 50%; background: var(--teal); }
  .client-name { color: var(--ink); font-size: 27px; line-height: 25px; font-weight: 700; letter-spacing: -0.5px; }
</style>
</head>
<body>
<main class="poster">
  <h1 class="headline">Lower the risk of COVID 19<br>in the workplace!</h1>
  <div class="rule rule-top"></div>
  <h2 class="title">BEWELL</h2>
  <div class="rule rule-mid"></div>

  <div class="timeline-spine"></div>
  <div class="tick" style="top:362px"></div>
  <div class="tick" style="top:468px"></div>
  <div class="tick" style="top:552px"></div>
  <div class="tick" style="top:649px"></div>
  <div class="tick" style="top:755px"></div>
  <div class="tick" style="top:860px"></div>

  <div class="tip-icon" style="top:328px" role="img" aria-label="Line icon of a steaming cup"></div>
  <p class="tip-text" style="top:333px">Bring your own cup<br>- don’t share cups and food.</p>

  <div class="tip-icon" style="top:435px" role="img" aria-label="Icon of a handshake crossed out"></div>
  <p class="tip-text" style="top:438px">Elbow tap instead of<br>handshakes and kisses</p>

  <div class="tip-icon" style="top:522px" role="img" aria-label="Line icon of hands being washed with water drops"></div>
  <p class="tip-text" style="top:542px">Wash your hands often - with soap</p>

  <div class="tip-icon" style="top:622px" role="img" aria-label="Icon of a figure coughing into an elbow"></div>
  <p class="tip-text" style="top:618px">Elbow or tissues when you cough<br>or sneeze then straight in the bin</p>

  <div class="tip-icon" style="top:724px" role="img" aria-label="Icon of a figure touching their face"></div>
  <p class="tip-text" style="top:724px">Leave your face alone after<br>touching shared surfaces</p>

  <div class="tip-icon" style="top:826px" role="img" aria-label="Icon of a head with a thermometer showing fever"></div>
  <p class="tip-text" style="top:828px">Leave your bugs at home if<br>you’re feeling unwell</p>

  <p class="healthline">Call health line if you have a cough, a high temperature<br>and shortness of breath. 0800 472 9160</p>

  <div class="rule rule-foot"></div>
  <p class="credits-label">Based on recommendations by</p>

  <div class="partner partner-dct">
    <span class="partner-shape"></span>
    <span class="partner-name">DCT</span>
  </div>
  <div class="partner partner-ipb">
    <span class="partner-shape"></span>
    <span class="partner-name">IPB</span>
  </div>

  <div class="client">
    <span class="client-mark"></span>
    <span class="client-name">Kindred<br>Works</span>
  </div>
</main>
</body>
</html>
```